Etiketten-Design für Honiggläser
Zielgruppe
Imkerei Lindner
Wir sind eine Familienbetrieb und vertreiben hochwertigen Honig aus eigener Imkerei
Aufgabenstellung
Es werden Etiketten für Honiggläser benötigt
Es gibt drei verschiedene Größen von Gläser (siehe Anhang) und je größe einmal „Frühtracht“ und einmal „Sommertracht“
Also insgesamt 6 Etiketten
500g Frühtracht und Sommertracht
250g Frühtracht und Sommertracht
150g Frühtracht und Sommertracht

```html
<!DOCTYPE html>
<html lang="de">
<head>
<meta charset="utf-8">
<title>Imkerei Lindner – Etiketten Frühtracht</title>
<link rel="stylesheet" href="https://fonts.googleapis.com/css2?family=Montserrat:wght@400;500;600&family=Amatic+SC:wght@700&display=swap">
<style>
  :root {
    --page: #f3f1ed;
    --label: #ffffff;
    --label-edge: #e4e1db;
    --ink: #2b2b2b;
    --honey: #e8913a;
    --organic: #8cc63f;
    --sketch-dark: #4a4a4a;
    --sketch-light: #d8d8d8;
    --comb: #eeeeee;
  }
  * { margin: 0; padding: 0; box-sizing: border-box; }
  html, body { width: 720px; height: 1200px; overflow: hidden; }
  body {
    background: var(--page);
    font-family: "Montserrat", sans-serif;
    color: var(--ink);
    position: relative;
  }
  .label {
    position: absolute;
    left: 20px;
    width: 680px;
    background: var(--label);
    border: 1px solid var(--label-edge);
    box-shadow: 0 6px 18px rgba(0,0,0,0.06);
    overflow: hidden;
  }
  .label--500 { top: 20px; height: 300px; }
  .label--250 { top: 340px; height: 250px; }
  .label--150 { top: 610px; height: 200px; left: 200px; width: 320px; }
  .label--comb { top: 830px; height: 250px; }

  .panel { position: absolute; top: 0; bottom: 0; }
  .sketch {
    position: absolute;
    background: radial-gradient(ellipse at center, var(--sketch-dark) 0%, #9a9a9a 45%, var(--sketch-light) 75%, transparent 100%);
    opacity: 0.75;
  }
  .sketch--flower {
    background: radial-gradient(circle at center, #6b6b6b 0%, #bcbcbc 30%, #ececec 65%, transparent 100%);
  }

  .info { font-size: 9.5px; line-height: 1.35; }
  .info p + p { margin-top: 9px; }
  .label--500 .info { font-size: 10.5px; white-space: nowrap; }

  .brand {
    font-family: "Montserrat", sans-serif;
    font-weight: 600;
    color: var(--honey);
    letter-spacing: 0.5px;
    text-transform: uppercase;
    text-align: center;
    line-height: 1.1;
  }
  .variety {
    font-family: "Amatic SC", cursive;
    font-weight: 700;
    color: var(--ink);
    text-align: center;
    letter-spacing: 1px;
  }
  .weight { font-size: 12px; font-weight: 500; text-align: center; }
  .organic-badge {
    width: 60px; height: 38px;
    background: var(--organic);
    margin: 8px auto;
  }
  .production { font-size: 9px; text-align: center; }

  .comb-fill {
    position: absolute;
    inset: 0;
    background: linear-gradient(90deg, var(--comb), #fafafa 40%, var(--comb));
    opacity: 0.8;
  }
</style>
</head>
<body>

<!-- 500 g -->
<section class="label label--500" aria-label="Etikett Frühtracht 500 g">
  <div class="panel" style="left:0; width:240px;">
    <div class="sketch" role="img" aria-label="Zeichnung einer Hummel" style="left:120px; top:20px; width:70px; height:60px;"></div>
    <div class="sketch sketch--flower" role="img" aria-label="Zeichnung einer Blüte" style="left:-40px; top:150px; width:100px; height:110px;"></div>
    <div class="info" style="position:absolute; left:62px; top:100px; width:200px;">
      <p>Lindner Wiesenweg 7 31708 Blütenfeld</p>
      <p>Info@imkereilindner.de<br>www.imkereilindner.de</p>
      <p>Lagerbedingungen:<br>dunkel, kühl und trocken</p>
      <p>Herkunft<br>Deutscher Honig aus eigener Imkerei</p>
    </div>
  </div>
  <div class="panel" style="left:270px; width:210px;">
    <div class="brand" style="position:absolute; top:60px; width:100%; font-size:16px;">Imkerei Lindner</div>
    <div class="variety" style="position:absolute; top:105px; width:100%; font-size:36px;">Frühtracht</div>
    <div class="sketch" role="img" aria-label="Zeichnung einer Biene" style="left:178px; top:90px; width:50px; height:42px;"></div>
    <div class="sketch" role="img" aria-label="Zeichnung einer Biene" style="left:5px; top:175px; width:45px; height:40px;"></div>
    <div class="sketch sketch--flower" role="img" aria-label="Zeichnung einer Blüte" style="left:130px; top:185px; width:100px; height:85px;"></div>
    <div class="weight" style="position:absolute; top:230px; width:100%;">netto 500g</div>
  </div>
  <div class="panel" style="left:520px; width:160px;">
    <div class="sketch" role="img" aria-label="Zeichnung einer Hummel" style="left:60px; top:20px; width:60px; height:55px;"></div>
    <div style="position:absolute; top:120px; width:100%;">
      <div class="organic-badge" role="img" aria-label="Bio-Siegel"></div>
      <div class="production">Produktionszeit:</div>
    </div>
  </div>
</section>

<!-- 250 g -->
<section class="label label--250" aria-label="Etikett Frühtracht 250 g">
  <div class="info" style="position:absolute; left:40px; top:55px; width:220px;">
    <p>Lindner Wiesenweg 7 31708 Blütenfeld</p>
    <p>Info@imkereilindner.de<br>www.imkereilindner.de</p>
    <p>Lagerbedingungen:<br>dunkel, kühl und trocken</p>
    <p>Herkunft<br>Deutscher Honig aus eigener Imkerei</p>
  </div>
  <div class="panel" style="left:260px; width:160px;">
    <div class="brand" style="position:absolute; top:30px; width:100%; font-size:14px;">Imkerei Lindner</div>
    <div class="sketch" role="img" aria-label="Zeichnung einer Hummel" style="left:25px; top:65px; width:110px; height:100px;"></div>
    <div class="variety" style="position:absolute; top:180px; width:100%; font-size:26px;">Frühtracht</div>
  </div>
  <div class="panel" style="left:500px; width:140px;">
    <div style="position:absolute; top:60px; width:100%;">
      <div class="weight">netto 250g</div>
      <div class="organic-badge" role="img" aria-label="Bio-Siegel"></div>
      <div class="production">Produktionszeit:</div>
    </div>
  </div>
</section>

<!-- 150 g -->
<section class="label label--150" aria-label="Etikett Frühtracht 150 g">
  <div class="panel" style="left:20px; width:160px;">
    <div class="brand" style="position:absolute; top:55px; width:100%; font-size:13px;">Imkerei Lindner</div>
    <div class="variety" style="position:absolute; top:85px; width:100%; font-size:26px;">Frühtracht</div>
    <div class="weight" style="position:absolute; top:125px; width:100%; font-size:11px;">netto 150g</div>
  </div>
  <div class="sketch" role="img" aria-label="Zeichnung einer Hummel" style="left:185px; top:35px; width:115px; height:110px;"></div>
</section>

<!-- 250 g mit Wabenhintergrund -->
<section class="label label--comb" aria-label="Etikett Frühtracht 250 g mit Waben">
  <div class="comb-fill" role="img" aria-label="Helles Wabenmuster"></div>
  <div class="info" style="position:absolute; left:40px; top:55px; width:220px;">
    <p>Lindner Wiesenweg 7 31708 Blütenfeld</p>
    <p>Info@imkereilindner.de<br>www.imkereilindner.de</p>
    <p>Lagerbedingungen:<br>dunkel, kühl und trocken</p>
    <p>Herkunft<br>Deutscher Honig aus eigener Imkerei</p>
  </div>
  <div class="panel" style="left:260px; width:160px;">
    <div class="brand" style="position:absolute; top:30px; width:100%; font-size:14px;">Imkerei Lindner</div>
    <div class="sketch" role="img" aria-label="Zeichnung einer Hummel" style="left:25px; top:65px; width:110px; height:100px;"></div>
    <div class="variety" style="position:absolute; top:180px; width:100%; font-size:26px;">Frühtracht</div>
  </div>
  <div class="panel" style="left:500px; width:140px;">
    <div style="position:absolute; top:60px; width:100%;">
      <div class="weight">netto 250g</div>
      <div class="organic-badge" role="img" aria-label="Bio-Siegel"></div>
      <div class="production">Produktionszeit:</div>
    </div>
  </div>
</section>

</body>
</html>
```